Veltrano Energy Business Card Design

website: www.veltranoenergy.example
Project: Business Card Design for Veltrano Energy
Name: Dorian Kettle
Title: Founder / Operations Strategist
Visual Identity & Logo:
Logo File: VEL-Logo-FullGradient-Final.png (Attached).
Color Palette: The brand relies on a distinctive Cyan (Blue) to Lime Green gradient.
Background Preference: We want a Dark Mode aesthetic (Deep Matte Black, Charcoal, or Dark Slate) to make the neon gradient of the logo pop. This feels more "tech/industrial" than a standard white card.
Design Aesthetic (The "Ops" Vibe):
Concept: "Grid & Infrastructure." We are a solar rental company, focusing on logistics and access.
Typography: White, bold sans-serif text for contact info. High contrast against the dark background.
Accents: Use the Cyan or Lime Green from the logo for thin divider lines or edge painting.
Avoid: No orange/gold (clashes with logo). No cartoon leaves.
Layout Requirements:
Front: Large, centered logo. Maybe a subtle UV gloss spot varnish over the logo icon.
Back: Name, Title, Contact Info.
Texture: Matte finish cardstock with gloss elements.
sample mock up of information on card: https://brivomarkco-my.filehost.example/:i:/g/personal/dorian_kettle_veltranoenergy_example/AbCdEfGhIjKlMnOpQrStUvWxYz012345678?e=Xy12Ab
Logo: https://brivomarkco.filehost.example/:i:/s/VeltranoEnergy/ZyXwVuTsRqPoNmLkJiHgFeDcBa9876543210?e=Pq34Cd

```html
<!DOCTYPE html>
<html lang="en">
<head>
<meta charset="utf-8">
<title>Veltrano Energy Business Card</title>
<link href="https://fonts.googleapis.com/css2?family=Open+Sans:wght@400;600;700&display=swap" rel="stylesheet">
<style>
  :root {
    --page: #3a3a3c;
    --card: #000000;
    --cyan: #1fb3c9;
    --blue: #1a8fd6;
    --lime: #8cc63f;
    --white: #ffffff;
    --soft: #e9e9e9;
  }
  * { box-sizing: border-box; margin: 0; padding: 0; }
  html, body { width: 1200px; height: 900px; overflow: hidden; }
  body {
    background: var(--page);
    font-family: "Open Sans", Arial, sans-serif;
    position: relative;
  }
  .card {
    position: absolute;
    width: 620px;
    height: 354px;
    background: var(--card);
    box-shadow: 0 12px 30px rgba(0,0,0,.55);
    overflow: hidden;
  }
  .card--info { left: 70px; top: 50px; }
  .card--brand { left: 510px; top: 496px; }

  .brand-mark {
    position: absolute;
    display: flex;
    align-items: center;
    gap: 12px;
  }
  .brand-mark__square {
    background: var(--cyan);
    flex: none;
  }
  .brand-mark__name {
    color: var(--cyan);
    font-weight: 400;
    letter-spacing: 1px;
    white-space: nowrap;
    line-height: 1;
  }
  .card--info .brand-mark { right: 44px; top: 40px; }
  .card--info .brand-mark__square { width: 30px; height: 30px; }
  .card--info .brand-mark__name { font-size: 30px; }
  .card--brand .brand-mark { left: 50%; top: 50%; transform: translate(-50%, -50%); gap: 18px; }
  .card--brand .brand-mark__square { width: 48px; height: 48px; }
  .card--brand .brand-mark__name { font-size: 50px; }

  .contact { position: absolute; left: 46px; top: 118px; }
  .contact__name {
    color: var(--lime);
    font-weight: 700;
    font-size: 17px;
    line-height: 22px;
    letter-spacing: .3px;
  }
  .contact__title { color: var(--soft); font-size: 14px; line-height: 19px; }
  .contact__company { color: var(--cyan); font-size: 14px; line-height: 19px; margin-top: 12px; }
  .contact__line { color: var(--soft); font-size: 14px; line-height: 20px; }
  .contact__row {
    display: flex; align-items: center; gap: 8px;
    color: var(--soft); font-size: 14px; line-height: 21px;
  }
  .contact__row--first { margin-top: 6px; }
  .contact__icon { width: 15px; height: 15px; flex: none; }

  .divider {
    position: absolute;
    left: 46px; right: 150px; top: 292px;
    height: 1px;
    background: linear-gradient(90deg, var(--cyan), var(--lime));
  }
  .tagline {
    position: absolute;
    left: 46px; top: 302px;
    color: var(--white);
    font-weight: 700;
    font-size: 15.5px;
    line-height: 21px;
    letter-spacing: .2px;
    white-space: nowrap;
  }

  .offices { position: absolute; right: 34px; top: 190px; text-align: center; }
  .offices__label { color: var(--cyan); font-weight: 700; font-size: 14px; line-height: 19px; margin-bottom: 4px; }
  .offices__flags { display: block; }
</style>
</head>
<body>

  <section class="card card--info" aria-label="Business card back">
    <div class="brand-mark">
      <span class="brand-mark__square"></span>
      <span class="brand-mark__name">Veltrano Energy</span>
    </div>

    <div class="contact">
      <p class="contact__name">DORIAN KETTLE</p>
      <p class="contact__title">Founder / Operations Strategist</p>
      <p class="contact__company">Veltrano Energy</p>
      <p class="contact__line">4120 Harlow Creek Drive</p>
      <p class="contact__line">Brinmoor, FL 30415</p>
      <p class="contact__row contact__row--first">
        <svg class="contact__icon" viewBox="0 0 24 24" aria-hidden="true">
          <path d="M6.6 10.8a15 15 0 0 0 6.6 6.6l2.2-2.2a1 1 0 0 1 1-.25 11.4 11.4 0 0 0 3.6.6 1 1 0 0 1 1 1V20a1 1 0 0 1-1 1A17 17 0 0 1 3 4a1 1 0 0 1 1-1h3.5a1 1 0 0 1 1 1c0 1.25.2 2.45.6 3.6a1 1 0 0 1-.25 1z" fill="var(--cyan)"/>
        </svg>
        555.014.2290
      </p>
      <p class="contact__row">
        <svg class="contact__icon" viewBox="0 0 24 24" aria-hidden="true" fill="none" stroke="var(--cyan)" stroke-width="1.6">
          <circle cx="12" cy="12" r="9"/>
          <ellipse cx="12" cy="12" rx="4" ry="9"/>
          <path d="M3 12h18M4.5 7.5h15M4.5 16.5h15"/>
        </svg>
        www.veltranoenergy.example
      </p>
    </div>

    <div class="divider"></div>
    <p class="tagline">No Debt, No Liens, No Maintenance, Just Savings.</p>

    <div class="offices">
      <p class="offices__label">Offices</p>
      <svg class="offices__flags" width="100" height="30" viewBox="0 0 100 30" role="img" aria-label="Round flag badges for the United States, United Kingdom and Canada offices">
        <circle cx="15" cy="15" r="14" fill="#b0253a" stroke="#fff" stroke-width="1.5"/>
        <circle cx="50" cy="15" r="14" fill="#1f3d8a" stroke="#fff" stroke-width="1.5"/>
        <circle cx="85" cy="15" r="14" fill="#d52b1e" stroke="#fff" stroke-width="1.5"/>
      </svg>
    </div>
  </section>

  <section class="card card--brand" aria-label="Business card front">
    <div class="brand-mark">
      <span class="brand-mark__square"></span>
      <span class="brand-mark__name">Veltrano Energy</span>
    </div>
  </section>

</body>
</html>
```